Logo, Web and Mobile Designs for enterprise social media platform

All the details are in the attached document, please start reading the scope document first which explains what is this project about and the details about the needed deliverables, after that please read the UI_Requirements document which will detail what is expected regarding the coded web version since this is a coded contest, it is very important that you meet the UI requirements or suggest something else but we will need to agree first before working on the coded version

Good Luck

Enterprise Social Media

Media

5+ page

Sans Serif

• All the must haves are listed in the scope document so please check before you start

```html
<!DOCTYPE html>
<html lang="en">
<head>
<meta charset="utf-8">
<title>Teamverse – Browse Events</title>
<link href="https://fonts.googleapis.com/css2?family=Roboto:ital,wght@0,300;0,400;0,500;0,700;1,300&display=swap" rel="stylesheet">
<style>
:root{
  --blue:#63b3f2;
  --blue-text:#4aa6ee;
  --page:#efefef;
  --white:#ffffff;
  --grey-text:#8a8a8a;
  --grey-light:#b8b8b8;
  --dark:#222222;
  --chip:#dedede;
  --line:#e4e4e4;
}
*{box-sizing:border-box;margin:0;padding:0}
html,body{width:741px;height:1200px;overflow:hidden}
body{position:relative;background:var(--page);font-family:'Roboto',sans-serif;color:var(--dark)}
.site-header{position:absolute;left:0;top:0;width:741px;height:51px;background:var(--blue)}
.brand{position:absolute;left:22px;top:17px;color:var(--white);font-weight:400;font-size:14px;letter-spacing:.3px}
.nav a{position:absolute;top:18px;color:var(--white);font-size:13px;text-decoration:none;letter-spacing:.3px}
.nav-icon{position:absolute;top:20px}
.hero{position:absolute;left:0;top:51px;width:741px;height:247px;background:linear-gradient(135deg,#b9aa98 0%,#8b6b4f 35%,#6a4530 60%,#9a4020 100%)}
.hero-btn{position:absolute;left:298px;top:109px;width:144px;height:30px;background:var(--blue);color:var(--white);font-size:22px;font-weight:300;text-align:center;line-height:30px}
.search-bar{position:absolute;left:0;top:298px;width:741px;height:42px;background:#fafafa}
.search-icon{position:absolute;left:21px;top:8px}
.search-placeholder{position:absolute;left:70px;top:9px;font-size:20px;font-weight:300;font-style:italic;color:var(--grey-light)}
.search-divider{position:absolute;left:622px;top:0;width:1px;height:42px;background:var(--line)}
.search-filter{position:absolute;left:643px;top:10px;font-size:18px;font-weight:300;font-style:italic;color:var(--grey-light)}
.search-chevron{position:absolute;left:709px;top:17px}
.section-title{position:absolute;left:0;top:361px;width:741px;text-align:center;font-size:18px;font-weight:400;color:var(--blue-text);letter-spacing:.5px}
.chip{position:absolute;top:404px;height:25px;border-radius:13px;background:var(--chip);font-size:11.5px;color:#444;line-height:25px;padding-left:11px}
.chip svg{position:absolute;right:6px;top:5px}
.filters{position:absolute;left:13px;top:447px}
.filter{position:absolute;left:0;width:110px;height:14px;font-size:9px;color:var(--grey-text);line-height:12px;padding-left:18px}
.filter svg{position:absolute;left:0;top:0}
.card{position:absolute;width:163px;height:208px;background:var(--white)}
.card-photo{position:absolute;left:0;top:0;width:163px;height:112px}
.card-title{position:absolute;left:6px;top:117px;font-size:16px;font-weight:300;color:var(--blue-text);white-space:nowrap}
.card-add{position:absolute;right:10px;top:122px}
.card-desc{position:absolute;left:6px;top:144px;width:92px;font-size:8px;line-height:10px;color:var(--grey-text)}
.card-more{position:absolute;right:10px;top:154px;font-size:8.5px;color:var(--blue-text)}
.card-actions{position:absolute;left:0;top:178px;width:163px;height:30px;border-top:1px solid #f2f2f2}
.card-actions span{position:absolute;top:10px;width:81px;text-align:center;font-size:8.5px}
.act-share{left:0;color:var(--blue-text)}
.act-invite{left:82px;color:var(--grey-text)}
.card-actions i{position:absolute;left:81px;top:0;width:1px;height:30px;background:var(--line)}
.card.is-selected .card-body{position:absolute;left:0;top:112px;width:163px;height:96px;background:var(--blue)}
.card.is-selected .card-title{color:var(--dark);font-weight:400}
.card.is-selected .card-desc,.card.is-selected .card-more,.card.is-selected .act-share{color:var(--white)}
.card.is-selected .act-invite{color:#a9d6f8}
.card.is-selected .card-actions{border-top-color:var(--blue)}
.card.is-selected .card-actions i{background:#8fc9f5}
.site-footer{position:absolute;left:0;top:1150px;width:741px;height:50px;background:var(--blue);color:var(--white)}
.footer-brand{position:absolute;left:22px;top:17px;font-size:14px;font-weight:400;letter-spacing:.3px}
.footer-note{position:absolute;left:0;width:741px;text-align:center;top:18px;font-size:13px}
</style>
</head>
<body>
<header class="site-header">
  <div class="brand">Teamverse</div>
  <nav class="nav">
    <a style="left:360px">HOME</a><a style="left:412px">EVENTS</a><a style="left:471px">GROUPS</a><a style="left:538px">BUSINESS</a><a style="left:614px">ABOUT</a>
  </nav>
  <svg class="nav-icon" style="left:677px" width="11" height="11" viewBox="0 0 11 11"><circle cx="5.5" cy="5.5" r="4" fill="#fff"/><circle cx="5.5" cy="5.5" r="1.6" fill="var(--blue)"/></svg>
  <svg class="nav-icon" style="left:709px" width="11" height="11" viewBox="0 0 11 11"><circle cx="5.5" cy="3" r="2.5" fill="#fff"/><path d="M0.5 11c0-3 2-4.5 5-4.5s5 1.5 5 4.5z" fill="#fff"/></svg>
</header>

<section class="hero" role="img" aria-label="Team working around a wooden table with laptops, notebooks and iced drinks">
  <div class="hero-btn">Create event</div>
</section>

<div class="search-bar">
  <svg class="search-icon" width="28" height="28" viewBox="0 0 28 28"><circle cx="11" cy="11" r="8" fill="none" stroke="#d6d6d6" stroke-width="2.5"/><line x1="17" y1="17" x2="26" y2="26" stroke="#d6d6d6" stroke-width="3"/></svg>
  <div class="search-placeholder">Search</div>
  <div class="search-divider"></div>
  <div class="search-filter">Events</div>
  <svg class="search-chevron" width="11" height="7" viewBox="0 0 11 7"><path d="M1 1l4.5 4.5L10 1" fill="none" stroke="#c4c4c4" stroke-width="1.5"/></svg>
</div>

<h1 class="section-title">BROWSE EVENTS</h1>

<div class="chip" style="left:118px;width:89px">Banking<svg width="15" height="15" viewBox="0 0 15 15"><circle cx="7.5" cy="7.5" r="7" fill="#9c9c9c"/><path d="M5 5l5 5M10 5l-5 5" stroke="#dedede" stroke-width="1.4"/></svg></div>
<div class="chip" style="left:218px;width:86px">Trading<svg width="15" height="15" viewBox="0 0 15 15"><circle cx="7.5" cy="7.5" r="7" fill="#9c9c9c"/><path d="M5 5l5 5M10 5l-5 5" stroke="#dedede" stroke-width="1.4"/></svg></div>
<div class="chip" style="left:315px;width:106px">Production<svg width="15" height="15" viewBox="0 0 15 15"><circle cx="7.5" cy="7.5" r="7" fill="#9c9c9c"/><path d="M5 5l5 5M10 5l-5 5" stroke="#dedede" stroke-width="1.4"/></svg></div>

<div class="filters">
  <div class="filter" style="top:0"><svg width="11" height="11"><rect x=".5" y=".5" width="10" height="10" rx="1" fill="none" stroke="#9a9a9a"/></svg>Construction</div>
  <div class="filter" style="top:26px"><svg width="11" height="11"><rect x=".5" y=".5" width="10" height="10" rx="1" fill="none" stroke="#9a9a9a"/></svg>Metal</div>
  <div class="filter" style="top:52px"><svg width="11" height="11"><rect x=".5" y=".5" width="10" height="10" rx="1" fill="none" stroke="#9a9a9a"/></svg>Jewlery</div>
  <div class="filter" style="top:79px"><svg width="11" height="11"><rect x=".5" y=".5" width="10" height="10" rx="1" fill="none" stroke="#9a9a9a"/></svg>Transport</div>
  <div class="filter" style="top:105px"><svg width="11" height="11"><rect width="11" height="11" rx="1" fill="#a8a8a8"/><path d="M2.5 5.5l2 2 4-4.5" fill="none" stroke="#fff" stroke-width="1.4"/></svg>Banking</div>
  <div class="filter" style="top:132px"><svg width="11" height="11"><rect width="11" height="11" rx="1" fill="#a8a8a8"/><path d="M2.5 5.5l2 2 4-4.5" fill="none" stroke="#fff" stroke-width="1.4"/></svg>Trading</div>
  <div class="filter" style="top:157px"><svg width="11" height="11"><rect width="11" height="11" rx="1" fill="#a8a8a8"/><path d="M2.5 5.5l2 2 4-4.5" fill="none" stroke="#fff" stroke-width="1.4"/></svg>Production</div>
</div>

<article class="card" style="left:118px;top:448px">
  <div class="card-photo" role="img" aria-label="Person writing in a notebook beside a laptop and a coffee cup" style="background:linear-gradient(135deg,#8f8a84,#d8d2c8 60%,#6d5e50)"></div>
  <div class="card-title">a-Prod hiring...</div>
  <svg class="card-add" width="10" height="10"><path d="M5 0v10M0 5h10" stroke="var(--blue-text)" stroke-width="1.3"/></svg>
  <div class="card-desc">a-Prod is hiring with an open and form...</div>
  <div class="card-more">READ MORE</div>
  <div class="card-actions"><span class="act-share">SHARE</span><i></i><span class="act-invite">INVITE</span></div>
</article>
<article class="card" style="left:289px;top:448px">
  <div class="card-photo" role="img" aria-label="Two colleagues meeting in a booth by large office windows" style="background:linear-gradient(180deg,#6f7378,#3f4246 60%,#8a8456)"></div>
  <div class="card-title">n-Bank partner...</div>
  <svg class="card-add" width="10" height="10"><path d="M5 0v10M0 5h10" stroke="var(--blue-text)" stroke-width="1.3"/></svg>
  <div class="card-desc">n-Bank partner meeting is taking place...</div>
  <div class="card-more">READ MORE</div>
  <div class="card-actions"><span class="act-share">SHARE</span><i></i><span class="act-invite">INVITE</span></div>
</article>
<article class="card" style="left:461px;top:448px">
  <div class="card-photo" role="img" aria-label="Hands over a wooden table with a red folder, laptop and drink" style="background:linear-gradient(135deg,#4a3326,#7b5a43 50%,#2e2420)"></div>
  <div class="card-title">x-Trade meet...</div>
  <svg class="card-add" width="10" height="10"><path d="M5 0v10M0 5h10" stroke="var(--blue-text)" stroke-width="1.3"/></svg>
  <div class="card-desc">x-Trade is throwing a meeting for...</div>
  <div class="card-more">READ MORE</div>
  <div class="card-actions"><span class="act-share">SHARE</span><i></i><span class="act-invite">INVITE</span></div>
</article>

<article class="card" style="left:118px;top:666px">
  <div class="card-photo" role="img" aria-label="Black and white view of people at a high-rise window over a city" style="background:linear-gradient(180deg,#2a2a2a,#8a8a8a 55%,#1c1c1c)"></div>
  <div class="card-title">GamaProd is sell...</div>
  <svg class="card-add" width="10" height="10"><path d="M5 0v10M0 5h10" stroke="var(--blue-text)" stroke-width="1.3"/></svg>
  <div class="card-desc">GamaProd is selling used material...</div>
  <div class="card-more">READ MORE</div>
  <div class="card-actions"><span class="act-share">SHARE</span><i></i><span class="act-invite">INVITE</span></div>
</article>
<article class="card is-selected" style="left:289px;top:666px">
  <div class="card-photo" role="img" aria-label="Meeting table with a bag, tablet, notebook and coffee cups" style="background:linear-gradient(180deg,#7a4a36,#b07a48 55%,#d49a5a)"></div>
  <div class="card-body"></div>
  <div class="card-title">Trade partners...</div>
  <svg class="card-add" width="12" height="10"><path d="M1 5l3.5 3.5L11 1" fill="none" stroke="#fff" stroke-width="1.4"/></svg>
  <div class="card-desc">Trade partners are meeting to discuss...</div>
  <div class="card-more">READ MORE</div>
  <div class="card-actions"><span class="act-share">SHARE</span><i></i><span class="act-invite">INVITE</span></div>
</article>
<article class="card" style="left:461px;top:666px">
  <div class="card-photo" role="img" aria-label="Legs of business people in dark suits walking on a street" style="background:linear-gradient(135deg,#d6d6d6,#bdbdbd 50%,#3a3a3a)"></div>
  <div class="card-title">Twin markets...</div>
  <svg class="card-add" width="10" height="10"><path d="M5 0v10M0 5h10" stroke="var(--blue-text)" stroke-width="1.3"/></svg>
  <div class="card-desc">Twin markets as a leading company...</div>
  <div class="card-more">READ MORE</div>
  <div class="card-actions"><span class="act-share">SHARE</span><i></i><span class="act-invite">INVITE</span></div>
</article>

<article class="card" style="left:118px;top:883px">
  <div class="card-photo" role="img" aria-label="Tablet and coffee cup on a white wooden desk" style="background:linear-gradient(135deg,#e8e8e8,#cfcfcf 60%,#a9a9a9)"></div>
  <div class="card-title">Brand &amp; repres...</div>
  <svg class="card-add" width="10" height="10"><path d="M5 0v10M0 5h10" stroke="var(--blue-text)" stroke-width="1.3"/></svg>
  <div class="card-desc">An business open discussion about...</div>
  <div class="card-more">READ MORE</div>
  <div class="card-actions"><span class="act-share">SHARE</span><i></i><span class="act-invite">INVITE</span></div>
</article>
<article class="card" style="left:289px;top:883px">
  <div class="card-photo" role="img" aria-label="Audience seen from behind at a business lecture" style="background:linear-gradient(135deg,#2a3a36,#5a6a60 50%,#2f5a4a)"></div>
  <div class="card-title">Business lect...</div>
  <svg class="card-add" width="10" height="10"><path d="M5 0v10M0 5h10" stroke="var(--blue-text)" stroke-width="1.3"/></svg>
  <div class="card-desc">Business succesful stories are about...</div>
  <div class="card-more">READ MORE</div>
  <div class="card-actions"><span class="act-share">SHARE</span><i></i><span class="act-invite">INVITE</span></div>
</article>
<article class="card" style="left:461px;top:883px">
  <div class="card-photo" role="img" aria-label="Hand holding a phone over a wooden cafe table" style="background:linear-gradient(135deg,#6a5a48,#9c8466 50%,#5a4a3a)"></div>
  <div class="card-title">Social media...</div>
  <svg class="card-add" width="10" height="10"><path d="M5 0v10M0 5h10" stroke="var(--blue-text)" stroke-width="1.3"/></svg>
  <div class="card-desc">Social media is helping businesses...</div>
  <div class="card-more">READ MORE</div>
  <div class="card-actions"><span class="act-share">SHARE</span><i></i><span class="act-invite">INVITE</span></div>
</article>

<footer class="site-footer">
  <div class="footer-brand">Teamverse l.l.c</div>
  <div class="footer-note">All rights reserved</div>
</footer>
</body>
</html>
```